Tallowreed Advisory Partners Business Card Design

We have the logo we just need someone to design a modern business card design.

Name: Desmond Munkalt
Phone: 3055550148
Mobile: 9175550193
Web:www.tallowreedadvisory.example
email: dmunkalt@tallowreedadvisory.example
Company: Tallowreed Advisory Partners
Title: CEO

Address: 718 Quillmore Ave, Miami, Florida 33190

Target Market(s)

companies over 100 employees

Industry/Entity Type

Business

```html
<!DOCTYPE html>
<html lang="en">
<head>
<meta charset="utf-8">
<title>Tallowreed Advisory Partners – Business Card</title>
<link rel="stylesheet" href="https://fonts.googleapis.com/css2?family=Cinzel:wght@400;500&family=Questrial&display=swap">
<style>
  :root {
    --backdrop: #8b8988;
    --card-dark: #17181b;
    --card-light: #f4f4f2;
    --brand-blue: #2f6ff0;
    --text-light: #e8e8ea;
    --text-muted: #c9c9cd;
    --text-dark: #1f1f22;
    --rule: #6d6e74;
  }
  * { box-sizing: border-box; margin: 0; padding: 0; }
  html, body {
    width: 1200px;
    height: 799px;
    overflow: hidden;
    background: var(--backdrop);
  }
  .card {
    position: absolute;
    box-shadow: 0 3px 8px rgba(0,0,0,0.35);
  }
  .card--front {
    left: 380px; top: 79px;
    width: 440px; height: 271px;
    background: var(--card-dark);
    color: var(--text-light);
  }
  .card--back {
    left: 388px; top: 444px;
    width: 424px; height: 259px;
    background: var(--card-light);
  }
  .brand-mark {
    position: absolute;
    border-radius: 50%;
    background: var(--brand-blue);
  }
  .card--front .brand-mark { left: 312px; top: 52px; width: 48px; height: 48px; }
  .card--back .brand-mark { left: 175px; top: 72px; width: 74px; height: 74px; }
  .brand-name, .brand-tagline {
    position: absolute;
    left: 0; right: 0;
    text-align: center;
    font-family: "Questrial", sans-serif;
    white-space: nowrap;
  }
  .card--front .brand-name {
    left: 236px; width: 200px;
    top: 104px; font-size: 17px; letter-spacing: 0.3px; color: var(--text-light);
  }
  .card--front .brand-tagline {
    left: 236px; width: 200px;
    top: 124px; font-size: 7px; letter-spacing: 0.3px; color: var(--text-light);
  }
  .card--back .brand-name {
    top: 160px; font-size: 25px; letter-spacing: 0.4px; color: var(--text-dark);
  }
  .card--back .brand-tagline {
    top: 190px; font-size: 9px; letter-spacing: 0.5px; color: var(--text-dark);
  }
  .holder-name {
    position: absolute; left: 46px; top: 127px;
    font-family: "Cinzel", serif; font-size: 14px; font-weight: 400; letter-spacing: 0.4px;
    color: var(--text-muted);
  }
  .holder-title {
    position: absolute; left: 46px; top: 144px;
    font-family: "Cinzel", serif; font-size: 9.5px; letter-spacing: 0.4px;
    color: var(--brand-blue);
  }
  .divider {
    position: absolute; left: 46px; top: 166px;
    width: 354px; height: 1px; background: var(--rule);
  }
  .contact-list {
    position: absolute; left: 50px; top: 174px;
    list-style: none;
    font-family: "Questrial", sans-serif; font-size: 11px; color: var(--text-muted);
  }
  .contact-list li {
    display: flex; align-items: center; height: 15.5px; white-space: nowrap;
  }
  .contact-icon { width: 9px; height: 9px; margin-right: 17px; fill: var(--brand-blue); }
  .address {
    position: absolute; right: 40px; top: 205px;
    text-align: right; font-style: normal;
    font-family: "Questrial", sans-serif; font-size: 10.5px; line-height: 15px;
    color: var(--text-muted);
  }
</style>
</head>
<body>
  <section class="card card--front" aria-label="Card front">
    <span class="brand-mark"></span>
    <p class="brand-name">TALLOWREED</p>
    <p class="brand-tagline">ADVISORY PARTNERS</p>

    <h1 class="holder-name">Desmond Munkalt</h1>
    <p class="holder-title">CEO</p>
    <span class="divider"></span>

    <ul class="contact-list">
      <li>
        <svg class="contact-icon" viewBox="0 0 10 10" aria-hidden="true"><path d="M1 3 Q5 0 9 3 L8 4.5 L6.5 3.8 L6.5 3 Q5 2.6 3.5 3 L3.5 3.8 L2 4.5 Z M2.5 5 H7.5 L8.5 9 H1.5 Z"/></svg>
        305-555-0148
      </li>
      <li>
        <svg class="contact-icon" viewBox="0 0 10 10" aria-hidden="true"><path d="M3 0.5 H7 Q7.8 0.5 7.8 1.3 V8.7 Q7.8 9.5 7 9.5 H3 Q2.2 9.5 2.2 8.7 V1.3 Q2.2 0.5 3 0.5 Z"/></svg>
        917-555-0193
      </li>
      <li>
        <svg class="contact-icon" viewBox="0 0 10 10" aria-hidden="true"><path d="M0.5 2 H9.5 V8 H0.5 Z M0.5 2 L5 5.5 L9.5 2" stroke="#17181b" stroke-width="0.8"/></svg>
        dmunkalt@tallowreedadvisory.example
      </li>
      <li>
        <svg class="contact-icon" viewBox="0 0 10 10" aria-hidden="true"><circle cx="5" cy="5" r="4.5"/><path d="M0.5 5 H9.5 M5 0.5 Q2 5 5 9.5 Q8 5 5 0.5" stroke="#17181b" stroke-width="0.7" fill="none"/></svg>
        www.tallowreedadvisory.example
      </li>
    </ul>

    <address class="address">
      718 Quillmore Ave<br>
      Miami, Florida 33190
    </address>
  </section>

  <section class="card card--back" aria-label="Card back">
    <span class="brand-mark"></span>
    <p class="brand-name">TALLOWREED</p>
    <p class="brand-tagline">ADVISORY PARTNERS</p>
  </section>
</body>
</html>
```